Professional Baby Bottle Bank Print Design

We need a baby bottle design that is 4.25" wide x 2.28" tall with a maximum of 6 colors (white is counted as a color).

The bottle design needs to be fun but professional. Bottles with cartoon images on it will be rejected immediately.

The bottle design wraps around the bottle. See examples here: https://kivora.shop/cat/InfantFlasks/TandemFlasks/5

Minimum font size is 10pt.

The bottle design must have the following text on it:
Main Text: Love them both
Paragraph text: Our ministry’s aim is to not only save unborn babies, but to provide love, support, and life-saving resources for vulnerable women in our community. By filling this bottle with cash, checks, and spare coins and returning it on collection day, you are truly saving and changing lives!
Optional text: Thank you!

We are including an example file and a template file. You do NOT have to use the template - but your file has to be the exact size mentioned. If you don't design as well as our sample, please don't waste our time by spamming us with hundreds of designs. We will ban design houses that spam us with designs that are more layouts (and not well designed).

Please note - white is a color. You don't have to do a box - but anything you don't make white will be see-through.

We will take the winners of this contest to a survey with the customers. We may choose two and edit the text of one slightly to be different. We must know the fonts used.

No gradients unless they are half-toned with relatively big sized dots.

Target Market(s)

Church Attendees coming from a Pregnancy Center

Industry/Entity Type

Religious Christian Churches

Requirements
Must have
• Professional, great palette, wording as described.
Nice to have
• Integrated design across the whole space with areas for text (no text all the way across)
Should not have
• Cartoon figures; elements shoved together that don't go together (i.e. - actually design something)

```html
<!DOCTYPE html>
<html lang="en">
<head>
<meta charset="utf-8">
<title>Love them both – Baby Bottle Wrap</title>
<link rel="stylesheet" href="https://fonts.googleapis.com/css2?family=Lobster&family=Oswald:wght@300&family=Dancing+Script:wght@500&display=swap">
<style>
  :root {
    --paper: #ffffff;
    --rose: #f25c86;
    --rose-soft: #f7a8bb;
    --rose-pale: #fbe4eb;
    --sky: #5bc3dc;
    --sky-soft: #bfe6f1;
    --ink: #25323d;
    --teal-ink: #1f4b52;
  }
  html, body {
    margin: 0;
    padding: 0;
    overflow: hidden;
    background: var(--paper);
  }
  .wrap {
    position: relative;
    width: 1200px;
    height: 644px;
    overflow: hidden;
    background: var(--paper);
  }
  .top-swoosh {
    position: absolute;
    left: 500px;
    top: 0;
    width: 700px;
    height: 100px;
  }
  .mother-art {
    position: absolute;
    left: 0;
    top: 34px;
    width: 555px;
    height: 610px;
    border-radius: 270px 270px 0 0;
    background: var(--rose-pale);
  }
  .headline {
    position: absolute;
    left: 590px;
    top: 94px;
    margin: 0;
    font-family: "Lobster", cursive;
    font-weight: 400;
    font-size: 102px;
    line-height: 1;
    color: var(--rose);
    white-space: nowrap;
  }
  .headline .accent { color: var(--sky); }
  .mission {
    position: absolute;
    right: 40px;
    top: 232px;
    margin: 0;
    font-family: "Oswald", sans-serif;
    font-weight: 300;
    font-size: 30px;
    line-height: 47px;
    letter-spacing: -0.4px;
    text-align: right;
    white-space: nowrap;
    color: var(--ink);
  }
  .sprig-art {
    position: absolute;
    left: 664px;
    top: 500px;
    width: 186px;
    height: 144px;
    border-radius: 93px 93px 0 0;
    background: var(--rose-pale);
  }
  .thanks {
    position: absolute;
    right: 42px;
    top: 550px;
    margin: 0;
    font-family: "Dancing Script", cursive;
    font-weight: 500;
    font-size: 42px;
    line-height: 1;
    color: var(--teal-ink);
  }
</style>
</head>
<body>
<main class="wrap">
  <svg class="top-swoosh" viewBox="0 0 700 100" aria-hidden="true">
    <path d="M40 0 C160 60 300 40 420 20 C520 5 600 30 700 70 L700 0 Z" fill="var(--sky-soft)" opacity="0.6"/>
    <path d="M200 0 C300 35 420 30 520 12 C590 2 650 10 700 30 L700 0 Z" fill="var(--rose-soft)" opacity="0.75"/>
    <path d="M560 0 C610 20 660 25 700 20 L700 0 Z" fill="var(--rose)" opacity="0.7"/>
  </svg>

  <div class="mother-art" role="img" aria-label="Line illustration of a mother with long pink hair cradling her sleeping newborn"></div>

  <h1 class="headline">Love them <span class="accent">both</span></h1>

  <p class="mission">Our ministry’s aim is to not only save unborn babies,<br>
  but to provide love, support, and life-saving<br>
  resources for vulnerable women in our community.<br>
  By filling this bottle with cash, checks, and spare<br>
  coins and returning it on collection day, you are truly<br>
  saving and changing lives!</p>

  <div class="sprig-art" role="img" aria-label="Small line drawing of leafy botanical sprigs"></div>

  <p class="thanks">Thank you!</p>
</main>
</body>
</html>
```